Womans Supplement Designs

Launching a Supplement company and need to get some initial designs created, I've attached our logo and the bottle type that I want the samples done one.

This project is for our Whey Protein we are starting with Vanilla, chocolate and strawberry banana

(ALL DESIGN VARIATIONS MUST BE A WHITE BOTTLE NOT BLACK)

(FOR DESIGN SAMPLES PLEASE USE THE SUPPLEMENT BOTTLE STYLE I PROVIDED)

Whoever is selected the winner I will have more work for you to complete the disigns for the rest of the products in the line, Just want to get this shake completed first

Target Market(s)

Women

Requirements
Must have
• Must have our current logo involved

the name of this product will be "KIVA LUM"

Must have this slogan,

ALL-IN-ONE PREMIUM PROTEIN NUTRITIONAL SHAKE FOR BLACK WOMEN

This is our meal replacement

the design should try to keep the same look and feel of the existing provided supplement images

we are starting with chocolate, vanilla and strawberry banana

this is for women and should look colorful and appeal to them
Should not have
• Do not use an image of a person or lady, don't want it branded to a person

```html
<!DOCTYPE html>
<html lang="en">
<head>
<meta charset="utf-8">
<title>KIVA LUM – Protein Shake Labels</title>
<link rel="stylesheet" href="https://fonts.googleapis.com/css2?family=Oswald:wght@400;500;700&family=Kaushan+Script&family=Lexend:wght@400;600&display=swap">
<style>
  :root {
    --page: #ffffff;
    --ink: #1c1c1c;
    --ink-soft: #3a3a3a;
    --label-bg: #ffffff;
    --choc-stripe: #8a3a16;
    --choc-band-a: #b87a35;
    --choc-band-b: #e6c48e;
    --choc-sub: #7a3418;
    --choc-sub-text: #e2a862;
    --choc-flavour: #8a3f1f;
    --van-stripe: #eadca4;
    --van-band-a: #c2c2c2;
    --van-band-b: #e4e4e4;
    --van-band-text: #666666;
    --van-sub: #efe4b8;
    --van-sub-text: #7a7a7a;
    --van-flavour: #d8c47c;
    --straw-stripe: #efb321;
    --straw-band-a: #e6ac1c;
    --straw-band-b: #f6d45a;
    --straw-sub: #d81f38;
    --straw-sub-text: #f2c948;
    --straw-flavour: #c8102e;
    --black-band: #111111;
  }
  * { box-sizing: border-box; margin: 0; padding: 0; }
  html, body { width: 1200px; height: 1200px; overflow: hidden; background: var(--page); }
  .range {
    width: 1200px; height: 1200px;
    display: flex; align-items: center; justify-content: center; gap: 20px;
  }
  .label {
    position: relative;
    width: 373px; height: 620px;
    background: var(--label-bg);
    box-shadow: 0 0 0 1px #e6e6e6;
    display: flex; flex-direction: column;
    overflow: hidden;
  }
  .label__stripe { height: 6px; background: var(--stripe); }
  .label--vanilla .label__stripe { height: 22px; }
  .label--strawberry .label__stripe { height: 10px; }

  .label__body { position: relative; flex: 1; padding: 34px 8px 0; }
  .panel {
    position: absolute; top: 100px;
    width: 66px;
    border: 1px solid #d6d6d6; padding: 4px;
    font-family: Oswald, sans-serif; color: var(--ink-soft);
    background: var(--label-bg);
  }
  .panel--info { left: 8px; }
  .panel--facts { right: 8px; }
  .panel__title { font-size: 8px; font-weight: 500; line-height: 1.1; margin-bottom: 3px; }
  .panel__text { font-size: 4.5px; line-height: 1.45; margin-bottom: 3px; }
  .panel__badges { display: flex; gap: 2px; margin-top: 4px; }
  .panel__badge { width: 9px; height: 9px; border-radius: 50%; border: 1px solid #8a8a8a; }
  .facts__row { display: flex; justify-content: space-between; font-size: 4.5px; border-bottom: 0.5px solid #888; padding: 1px 0; }
  .facts__head { background: #444; color: #fff; font-size: 4.5px; padding: 1px 2px; margin-bottom: 2px; }
  .panel__squares { display: flex; gap: 2px; margin-top: 4px; }
  .panel__square { width: 7px; height: 7px; background: #444; }

  .front { text-align: center; }
  .brand { display: flex; align-items: center; justify-content: center; gap: 7px; height: 58px; }
  .brand__dot { width: 14px; height: 14px; border-radius: 50%; border: 2px solid var(--ink-soft); }
  .brand__name { font-family: Lexend, sans-serif; font-weight: 400; font-size: 12px; letter-spacing: 1px; color: var(--ink-soft); }
  .product-name {
    font-family: Oswald, sans-serif; font-weight: 700;
    font-size: 58px; line-height: 1; letter-spacing: 0;
    color: var(--ink); margin-top: 22px; white-space: nowrap;
  }
  .slogan {
    font-family: Oswald, sans-serif; font-weight: 500;
    font-size: 14px; line-height: 1.12; color: var(--ink);
    margin-top: 24px; text-transform: uppercase;
  }
  .flavour {
    font-family: "Kaushan Script", cursive;
    font-size: 26px; line-height: 1.2; color: var(--flavour); margin-top: 10px; white-space: nowrap;
  }

  .band {
    height: 38px; display: flex; align-items: center; justify-content: center;
    background: linear-gradient(90deg, var(--band-a), var(--band-b));
    font-family: Lexend, sans-serif; font-weight: 600; font-size: 19px;
    color: #fff; letter-spacing: 0.5px;
  }
  .label--vanilla .band { color: var(--van-band-text); }
  .claims {
    height: 38px; background: var(--sub);
    display: flex; align-items: center; justify-content: center; gap: 10px;
    font-family: Lexend, sans-serif; font-size: 9px; line-height: 1.1;
    color: var(--sub-text); text-align: center;
  }
  .claims__dot { width: 4px; height: 4px; border-radius: 50%; background: #fff; }
  .net-weight {
    height: 42px; background: var(--black-band);
    display: flex; align-items: center; justify-content: center;
    font-family: Lexend, sans-serif; font-weight: 600; font-size: 14px; color: #fff;
  }
  .label__foot { height: 30px; }

  .label--chocolate { --stripe: var(--choc-stripe); --band-a: var(--choc-band-a); --band-b: var(--choc-band-b); --sub: var(--choc-sub); --sub-text: var(--choc-sub-text); --flavour: var(--choc-flavour); }
  .label--vanilla { --stripe: var(--van-stripe); --band-a: var(--van-band-a); --band-b: var(--van-band-b); --sub: var(--van-sub); --sub-text: var(--van-sub-text); --flavour: var(--van-flavour); }
  .label--strawberry { --stripe: var(--straw-stripe); --band-a: var(--straw-band-a); --band-b: var(--straw-band-b); --sub: var(--straw-sub); --sub-text: var(--straw-sub-text); --flavour: var(--straw-flavour); }
</style>
</head>
<body>
<main class="range">

  <section class="label label--chocolate">
    <div class="label__stripe"></div>
    <div class="label__body">
      <div class="front">
        <div class="brand"><span class="brand__dot"></span><p class="brand__name">AMARA BLOOM</p></div>
        <h1 class="product-name">KIVA LUM</h1>
        <p class="slogan">All-in-one premium protein<br>nutritional shake<br>for black women</p>
        <p class="flavour">Chocolate</p>
      </div>
      <aside class="panel panel--info">
        <p class="panel__title">DIETARY SUPPLEMENT</p>
        <p class="panel__text">Ingredients: whey protein blend, natural flavour, sweetener, sunflower lecithin.</p>
        <p class="panel__text">Storage: keep in a cool dry place.</p>
        <p class="panel__text">Use: mix one scoop with water or milk after training.</p>
        <p class="panel__text">Not a substitute for a varied balanced diet.</p>
        <div class="panel__badges"><span class="panel__badge"></span><span class="panel__badge"></span><span class="panel__badge"></span></div>
      </aside>
      <aside class="panel panel--facts">
        <p class="panel__title">Nutrition Facts</p>
        <p class="facts__head">Serving Size 1 scoop</p>
        <p class="facts__row"><span>Calories</span><span>130</span></p>
        <p class="facts__row"><span>Total Fat</span><span>2g</span></p>
        <p class="facts__row"><span>Sodium</span><span>90mg</span></p>
        <p class="facts__row"><span>Total Carbs</span><span>4g</span></p>
        <p class="facts__row"><span>Protein</span><span>24g</span></p>
        <p class="facts__row"><span>Calcium</span><span>8%</span></p>
        <p class="panel__text">Daily values based on a 2000 calorie diet.</p>
        <div class="panel__squares"><span class="panel__square"></span><span class="panel__square"></span><span class="panel__square"></span><span class="panel__square"></span></div>
      </aside>
    </div>
    <div class="band">DIETARY SUPPLEMENT</div>
    <div class="claims"><span>GLUTEN<br>FREE</span><span class="claims__dot"></span><span>SOY<br>FREE</span><span class="claims__dot"></span><span>DAIRY<br>FREE</span><span class="claims__dot"></span><span>VEGAN</span></div>
    <div class="net-weight">NET WT. 5 LBS (2.26 KG)</div>
    <div class="label__foot"></div>
  </section>

  <section class="label label--vanilla">
    <div class="label__stripe"></div>
    <div class="label__body">
      <div class="front">
        <div class="brand"><span class="brand__dot"></span><p class="brand__name">AMARA BLOOM</p></div>
        <h1 class="product-name">KIVA LUM</h1>
        <p class="slogan">All-in-one premium protein<br>nutritional shake<br>for black women</p>
        <p class="flavour">Vanilla</p>
      </div>
      <aside class="panel panel--info">
        <p class="panel__title">DIETARY SUPPLEMENT</p>
        <p class="panel__text">Ingredients: whey protein blend, natural flavour, sweetener, sunflower lecithin.</p>
        <p class="panel__text">Storage: keep in a cool dry place.</p>
        <p class="panel__text">Use: mix one scoop with water or milk after training.</p>
        <p class="panel__text">Not a substitute for a varied balanced diet.</p>
        <div class="panel__badges"><span class="panel__badge"></span><span class="panel__badge"></span><span class="panel__badge"></span></div>
      </aside>
      <aside class="panel panel--facts">
        <p class="panel__title">Nutrition Facts</p>
        <p class="facts__head">Serving Size 1 scoop</p>
        <p class="facts__row"><span>Calories</span><span>130</span></p>
        <p class="facts__row"><span>Total Fat</span><span>2g</span></p>
        <p class="facts__row"><span>Sodium</span><span>90mg</span></p>
        <p class="facts__row"><span>Total Carbs</span><span>4g</span></p>
        <p class="facts__row"><span>Protein</span><span>24g</span></p>
        <p class="facts__row"><span>Calcium</span><span>8%</span></p>
        <p class="panel__text">Daily values based on a 2000 calorie diet.</p>
        <div class="panel__squares"><span class="panel__square"></span><span class="panel__square"></span><span class="panel__square"></span><span class="panel__square"></span></div>
      </aside>
    </div>
    <div class="band">DIETARY SUPPLEMENT</div>
    <div class="claims"><span>GLUTEN<br>FREE</span><span class="claims__dot"></span><span>SOY<br>FREE</span><span class="claims__dot"></span><span>DAIRY<br>FREE</span><span class="claims__dot"></span><span>VEGAN</span></div>
    <div class="net-weight">NET WT. 5 LBS (2.26 KG)</div>
    <div class="label__foot"></div>
  </section>

  <section class="label label--strawberry">
    <div class="label__stripe"></div>
    <div class="label__body">
      <div class="front">
        <div class="brand"><span class="brand__dot"></span><p class="brand__name">AMARA BLOOM</p></div>
        <h1 class="product-name">KIVA LUM</h1>
        <p class="slogan">All-in-one premium protein<br>nutritional shake<br>for black women</p>
        <p class="flavour">Strawberry Banana</p>
      </div>
      <aside class="panel panel--info">
        <p class="panel__title">DIETARY SUPPLEMENT</p>
        <p class="panel__text">Ingredients: whey protein blend, natural flavour, sweetener, sunflower lecithin.</p>
        <p class="panel__text">Storage: keep in a cool dry place.</p>
        <p class="panel__text">Use: mix one scoop with water or milk after training.</p>
        <p class="panel__text">Not a substitute for a varied balanced diet.</p>
        <div class="panel__badges"><span class="panel__badge"></span><span class="panel__badge"></span><span class="panel__badge"></span></div>
      </aside>
      <aside class="panel panel--facts">
        <p class="panel__title">Nutrition Facts</p>
        <p class="facts__head">Serving Size 1 scoop</p>
        <p class="facts__row"><span>Calories</span><span>130</span></p>
        <p class="facts__row"><span>Total Fat</span><span>2g</span></p>
        <p class="facts__row"><span>Sodium</span><span>90mg</span></p>
        <p class="facts__row"><span>Total Carbs</span><span>4g</span></p>
        <p class="facts__row"><span>Protein</span><span>24g</span></p>
        <p class="facts__row"><span>Calcium</span><span>8%</span></p>
        <p class="panel__text">Daily values based on a 2000 calorie diet.</p>
        <div class="panel__squares"><span class="panel__square"></span><span class="panel__square"></span><span class="panel__square"></span><span class="panel__square"></span></div>
      </aside>
    </div>
    <div class="band">DIETARY SUPPLEMENT</div>
    <div class="claims"><span>GLUTEN<br>FREE</span><span class="claims__dot"></span><span>SOY<br>FREE</span><span class="claims__dot"></span><span>DAIRY<br>FREE</span><span class="claims__dot"></span><span>VEGAN</span></div>
    <div class="net-weight">NET WT. 5 LBS (2.26 KG)</div>
    <div class="label__foot"></div>
  </section>

</main>
</body>
</html>
```